Luxury Business Card Design for High-End Window Treatments

Gilded Vantages
Custom Plantation Shutters & Architectural Shading Systems

⸻

BACK

Daniel Forsythe
Owner

Custom Interior & Exterior Window Treatments

919-482-7034
gildedvantages.com

I have included a picture that I’m hoping we can use on the back, but I’m also wondering if you can get rid of the ladder? Should we get rid of shutters , shades and blinds underneath Gilded Vantages?

Target Market(s)

High-end residential homeowners, custom home builders, architects, interior designers, and luxury renovation clients seeking premium plantation shutters and motorized architectural shading systems.

Industry/Entity Type

Custom Window treatments

Contact Information for Business Card

Front Gilded Vantages Custom Plantation Shutters Motorized Architectural Shading Systems BACK Daniel Forsythe Owner 919-482-7034 GildedVantages.com Custom Interior & Exterior Window Treatments By Appointment

Requirements
Nice to have
• Not 100% sure on nice to halves or the color but you can definitely check out my website to get a better understanding of what I’m trying to do

```html
<!DOCTYPE html>
<html lang="en">
<head>
<meta charset="utf-8">
<title>Gilded Vantages – Business Card</title>
<link rel="stylesheet" href="https://fonts.googleapis.com/css2?family=Playfair+Display:wght@500&family=Urbanist:wght@400;500;600&family=Allura&display=swap">
<style>
  :root {
    --backdrop: #e2e2e2;
    --card-black: #050505;
    --gold: #e9c557;
    --gold-deep: #6b5a1c;
    --cream: #ece4d6;
    --white: #f4f1ea;
    --sky: #5a7fa8;
    --foliage: #2e3a2c;
  }
  * { margin: 0; padding: 0; box-sizing: border-box; }
  html, body {
    width: 804px; height: 1200px; overflow: hidden;
    background: var(--backdrop);
    font-family: "Urbanist", sans-serif;
  }
  .canvas { position: relative; width: 804px; height: 1200px; }

  .card {
    position: absolute; left: 82px; width: 640px; height: 366px;
    overflow: hidden;
  }
  .card-front {
    top: 196px;
    background:
      radial-gradient(ellipse 60% 80% at 100% 45%, rgba(122,100,30,0.75), transparent 70%),
      radial-gradient(ellipse 40% 50% at 0% 0%, rgba(90,75,25,0.45), transparent 70%),
      var(--card-black);
  }
  .card-back { top: 638px; background: var(--card-black); }

  /* Front */
  .brand-title {
    position: absolute; left: 0; right: 0; top: 52px; text-align: center;
    font-family: "Playfair Display", serif; font-weight: 500;
    font-size: 56px; color: var(--cream); letter-spacing: 0.5px; line-height: 1;
  }
  .brand-script {
    position: absolute; left: 0; right: 0; top: 96px; text-align: center;
    font-family: "Allura", cursive; font-size: 50px; color: var(--gold); line-height: 1;
  }
  .divider {
    position: absolute; left: 150px; width: 340px; top: 144px; height: 1px;
    background: linear-gradient(90deg, transparent, var(--gold) 50%, transparent);
  }
  .brand-tagline {
    position: absolute; left: 0; right: 0; top: 153px; text-align: center;
    font-size: 21px; color: var(--white); font-weight: 400;
  }
  .brand-name-mark {
    position: absolute; left: 56px; top: 262px;
    font-size: 24px; font-weight: 400; color: var(--gold); line-height: 1;
  }
  .contact { position: absolute; left: 380px; top: 236px; }
  .contact-name {
    font-size: 18px; font-weight: 600; color: var(--gold); margin-bottom: 6px;
  }
  .contact-line {
    display: flex; align-items: center; gap: 8px;
    font-size: 18px; color: var(--white); margin-bottom: 4px;
  }
  .contact-line svg { width: 13px; height: 13px; fill: var(--gold); flex: none; }

  /* Back */
  .back-photo {
    position: absolute; inset: 0;
    background:
      linear-gradient(180deg, rgba(0,0,0,0) 0%, rgba(0,0,0,0.35) 45%, rgba(0,0,0,0.9) 85%, #000 100%),
      linear-gradient(180deg, var(--sky) 0%, #8a8a80 20%, #3a3f46 45%, var(--foliage) 70%, #111 100%);
  }
  .back-headline {
    position: absolute; left: 0; right: 0; top: 162px; text-align: center;
    font-size: 35px; font-weight: 600; color: var(--gold); line-height: 1;
  }
  .back-subline {
    position: absolute; left: 0; right: 0; top: 196px; text-align: center;
    white-space: nowrap; line-height: 1;
  }
  .back-subline .script {
    font-family: "Allura", cursive; font-size: 36px; color: var(--white);
  }
  .back-subline .plain {
    font-size: 23px; font-weight: 600; color: var(--white); margin-left: 8px;
  }
  .back-name {
    position: absolute; left: 76px; top: 301px;
    font-size: 21px; font-weight: 600; color: var(--gold);
  }
  .back-contact { position: absolute; left: 386px; top: 274px; }
  .back-role {
    display: flex; align-items: baseline; gap: 14px;
    color: var(--white); margin-bottom: 6px;
  }
  .back-role .role { font-size: 22px; font-weight: 500; }
  .back-role .phone { font-size: 17px; }
</style>
</head>
<body>
<main class="canvas">

  <section class="card card-front" aria-label="Card front">
    <h1 class="brand-title">Gilded Vantages</h1>
    <p class="brand-script">Custom Plantation Shutters</p>
    <div class="divider"></div>
    <p class="brand-tagline">Motorized Architectural Shading Systems</p>

    <p class="brand-name-mark">Gilded Vantages</p>

    <div class="contact">
      <p class="contact-name">Daniel Forsythe</p>
      <p class="contact-line">
        <svg viewBox="0 0 24 24" aria-hidden="true"><path d="M6.6 10.8a15.1 15.1 0 0 0 6.6 6.6l2.2-2.2a1 1 0 0 1 1-.25 11.4 11.4 0 0 0 3.6.57 1 1 0 0 1 1 1V20a1 1 0 0 1-1 1A17 17 0 0 1 3 4a1 1 0 0 1 1-1h3.5a1 1 0 0 1 1 1c0 1.25.2 2.45.57 3.6a1 1 0 0 1-.25 1z"/></svg>
        919 482 7034
      </p>
      <p class="contact-line">
        <svg viewBox="0 0 24 24" aria-hidden="true"><path d="M4 2l16 9-7 1.5 4 8-3 1.5-4-8L4 19z"/></svg>
        gildedvantages.com
      </p>
    </div>
  </section>

  <section class="card card-back" aria-label="Card back">
    <div class="back-photo" role="img" aria-label="Photo of a white two-storey porch fitted with dark motorized exterior shades, trees and blue sky behind"></div>
    <h2 class="back-headline">Custom Interior &amp; Exterior</h2>
    <p class="back-subline"><span class="script">Window Treatments</span><span class="plain">By Appointment</span></p>
    <p class="back-name">Daniel Forsythe</p>
    <div class="back-contact">
      <p class="back-role"><span class="role">Owner</span><span class="phone">919-482-7034</span></p>
      <p class="contact-line">
        <svg viewBox="0 0 24 24" aria-hidden="true"><path d="M4 2l16 9-7 1.5 4 8-3 1.5-4-8L4 19z"/></svg>
        gildedvantages.com
      </p>
    </div>
  </section>

</main>
</body>
</html>
```